Präsentationsvorlagen für Unternehmensberater
Zielgruppe
Ich bin selbstständiger Unternehmensberater / Freelancer / Projektmanager / Interimmanager und Trainer in den Bereichen operative Logistik und Logistik-IT. Meine Kundenmix reicht vom Kleinunternehmen bis hin zu multinationalen Konzernen. Meine Projekte führen mich nach ganz Europa, mit Schwerpunkten im Osten. Als Projektsprachen verwende ich deutsch und englisch.
Aufgabenstellung
Ich suche nach einem umfangreichen Powerpoint-Masterfile zur Verwendung sowohl in der Aquisitionsphase als auch in den Projekten. Das moderne Design muss am Corporate Design angelehnt sein (siehe beiliegende Dateien, Webpage ist noch in Entwicklung, die aktuelle Layoutplanung ist aber verfügbar und kann bei Bedarf übermittelt werden). Geschwungene Formen bevorzuge ich gegenüber gradliniger Geometrie. Ein wenig verspielt darf es sein, ohne jedoch an Professionalität einzubüßen.
Folgendes soll im Masterfile berücksichtigt werden:
Aufbau:
- Dreistufige Struktur (Titel / Bereich / Thema)
- verborgene Folien / direkter Klick auf Themen z.B. von Inhaltsverzeichnis werden genutzt
- Animationen werden verwendet
- Seitenverhältnis 16:9
aktuell geplante Folientypen (Vorlage für alle Typen gewünscht):
- Agenda
- Übersicht / Inhalt
- Text/Aufzählung
- Zeitleiste
- Bilder mit/ohne Textspalte
- eingebundenes Video mit/ohne Text
- Darstellung ineinandergreifender Themen (ähnlich Puzzle)
- Diagramme (Kreisdiagramm, Balkendiagramm, Liniendiagramm, Spiderweb) jeweils mit und ohne Textspalte
- Gegenüberstellungen (z.B. Vor- und Nachteile)
- Wordcloud
- Prozessschritte
- Flowcharts
- Tabellen
- magisches Dreick/Vieleck (Darstellung untereinander konkurrierenden Ziele)
- Slogans / Zitate / Hypothesen
- Mengenüberschneidungen
- Call to Action
- Schlussfolie / Fragen?
- Kontaktdaten

```html
<!DOCTYPE html>
<html lang="de">
<head>
<meta charset="utf-8">
<title>Agenda</title>
<link href="https://fonts.googleapis.com/css2?family=Lato:wght@400;700&display=swap" rel="stylesheet">
<style>
  :root {
    --stage: #dedede;
    --paper: #ffffff;
    --band: #27a9e1;
    --cyan: #00c3f7;
    --blue: #0aa3dc;
    --grey: #a6a6a6;
    --heading: #333333;
    --body: #7a7a7a;
    --white: #ffffff;
  }
  * { box-sizing: border-box; margin: 0; padding: 0; }
  html, body {
    width: 1200px; height: 730px; overflow: hidden;
    background: var(--stage);
    font-family: "Lato", Arial, sans-serif;
  }
  .stage { position: relative; width: 1200px; height: 730px; }
  .slide {
    position: absolute; left: 59.6px; top: 59.6px;
    width: 1197px; height: 673px;
    background: var(--paper);
    overflow: hidden;
    transform: scale(0.9031);
    transform-origin: 0 0;
  }
  .slide-shapes { position: absolute; inset: 0; width: 1197px; height: 673px; }
  .slide-title {
    position: absolute; left: 46px; top: 34px;
    color: var(--white); font-size: 35px; font-weight: 700;
  }
  .brand {
    position: absolute; right: 18px; top: 18px;
    display: flex; align-items: center; gap: 8px;
  }
  .brand-name { color: var(--band); font-size: 16px; font-weight: 700; }
  .brand-dot { width: 44px; height: 44px; border-radius: 50%; border: 3px solid var(--band); }
  .agenda-item { position: absolute; width: 420px; height: 78px; }
  .item-number {
    position: absolute; left: 0; top: 0;
    width: 76px; height: 76px; border-radius: 50%;
    display: flex; align-items: center; justify-content: center;
    color: var(--white); font-size: 20px; font-weight: 700;
  }
  .item-number.cyan { background: var(--cyan); }
  .item-number.blue { background: var(--blue); }
  .item-number.grey { background: var(--grey); }
  .item-text { position: absolute; left: 89px; top: 4px; }
  .item-heading { color: var(--heading); font-size: 20px; font-weight: 700; line-height: 26px; }
  .item-body { color: var(--body); font-size: 13.5px; line-height: 18.5px; margin-top: 2px; }
  .footer {
    position: absolute; left: 0; right: 0; top: 648px;
    color: var(--white); font-size: 13px; letter-spacing: 4.5px;
  }
  .footer span { position: absolute; }
  .footer-title { left: 22px; }
  .footer-date { left: 522px; }
  .footer-page { right: 20px; }
</style>
</head>
<body>
<div class="stage">
  <section class="slide">
    <svg class="slide-shapes" viewBox="0 0 1197 673" aria-hidden="true">
      <path fill="var(--band)" d="M0 0 H568 C548 20 538 42 538 72 L538 102 C538 132 508 144 458 144 C378 144 300 120 200 120 C120 120 44 126 0 134 Z"/>
      <path fill="var(--band)" d="M0 612 C80 630 160 642 260 640 C480 636 760 570 1000 570 C1080 570 1150 582 1197 593 V673 H0 Z"/>
    </svg>

    <h1 class="slide-title">Agenda</h1>

    <div class="brand">
      <span class="brand-name">Kelvaro</span>
      <span class="brand-dot"></span>
    </div>

    <div class="agenda-item" style="left:136px; top:199px;">
      <div class="item-number cyan">01</div>
      <div class="item-text"><h2 class="item-heading">Subtitle demo text</h2><p class="item-body">Lorem ipsum dolor sed do sit amet, consectetur<br>adipiscing elit, sed do eiusmod tempor sed re eu</p></div>
    </div>
    <div class="agenda-item" style="left:134px; top:324px;">
      <div class="item-number blue">02</div>
      <div class="item-text"><h2 class="item-heading">Subtitle demo text</h2><p class="item-body">Lorem ipsum dolor sed do sit amet, consectetur<br>adipiscing elit, sed do eiusmod tempor sed re eu</p></div>
    </div>
    <div class="agenda-item" style="left:136px; top:448px;">
      <div class="item-number grey">03</div>
      <div class="item-text"><h2 class="item-heading">Subtitle demo text</h2><p class="item-body">Lorem ipsum dolor sed do sit amet, consectetur<br>adipiscing elit, sed do eiusmod tempor sed re eu</p></div>
    </div>
    <div class="agenda-item" style="left:624px; top:199px;">
      <div class="item-number grey">04</div>
      <div class="item-text"><h2 class="item-heading">Subtitle demo text</h2><p class="item-body">Lorem ipsum dolor sed do sit amet, consectetur<br>adipiscing elit, sed do eiusmod tempor sed re eu</p></div>
    </div>
    <div class="agenda-item" style="left:622px; top:324px;">
      <div class="item-number blue">05</div>
      <div class="item-text"><h2 class="item-heading">Subtitle demo text</h2><p class="item-body">Lorem ipsum dolor sed do sit amet, consectetur<br>adipiscing elit, sed do eiusmod tempor sed re eu</p></div>
    </div>
    <div class="agenda-item" style="left:624px; top:448px;">
      <div class="item-number cyan">06</div>
      <div class="item-text"><h2 class="item-heading">Subtitle demo text</h2><p class="item-body">Lorem ipsum dolor sed do sit amet, consectetur<br>adipiscing elit, sed do eiusmod tempor sed re eu</p></div>
    </div>

    <footer class="footer">
      <span class="footer-title">Präsentationstitel</span>
      <span class="footer-date">01/02/2020</span>
      <span class="footer-page">02</span>
    </footer>
  </section>
</div>
</body>
</html>
```